Disability and mental health support work company requires business card

Specialising
Wrenfield Disability is a new QCAP service aimed toward QCAP participants with a history of criminal justice, psychosocial/mental health, intellectual, and cognitive disabilities.

Our focus
Focusing on providing core QCAP supports for community participation, daily activities and supported independent living.

Authentic
Likeminded people wanting to make a difference in participant's lives.

Our aim to provide holistic and empowering supports targeted towards creating independence and guidance for all participants and families.
Over 35 years of experience working with people that have psychosocial, intellectual, and cognitive disabilities.

Industry/Entity Type

disability and mental health

Contact Information for Business Card

logo - business name

Colors
0054AA
0677BA
7BADD7
CADEEF
E8F1F8
FFF300
FFF600
FEFA6F
FFFEC7
FFFEE8

Requirements
Must have
• want double sided business cards(wont let me change it)
Should not have
• any disability related pictures

```html
<!DOCTYPE html>
<html lang="en">
<head>
<meta charset="utf-8">
<title>Wrenfield Disability – Business Card</title>
<link rel="stylesheet" href="https://fonts.googleapis.com/css2?family=DM+Serif+Display&family=Mulish:wght@400;500;600&display=swap">
<style>
  :root {
    --navy: #14365c;
    --sky: #6fa3d8;
    --gold: #e8b030;
    --ink: #1a2a44;
    --paper: #ffffff;
    --backdrop: #e4e1e3;
  }
  * { margin: 0; padding: 0; box-sizing: border-box; }
  html, body { width: 1200px; height: 900px; overflow: hidden; }
  body {
    background: var(--backdrop);
    font-family: "Mulish", sans-serif;
    display: flex;
    flex-direction: column;
    align-items: center;
    justify-content: center;
    gap: 50px;
  }
  .card {
    position: relative;
    width: 640px;
    height: 368px;
    border-radius: 18px;
    overflow: hidden;
  }
  .card--front { background: var(--paper); }
  .card--back { background: var(--navy); }

  .brand-mark {
    position: absolute;
    border-radius: 50%;
    display: flex;
    flex-direction: column;
    align-items: center;
    justify-content: center;
    text-align: center;
    font-family: "DM Serif Display", serif;
    color: var(--sky);
    line-height: 1.05;
  }
  .card--front .brand-mark {
    left: 80px; top: 81px;
    width: 204px; height: 204px;
    background: var(--navy);
    font-size: 25px;
  }
  .card--back .brand-mark {
    left: 220px; top: 82px;
    width: 200px; height: 200px;
    border: 3px solid var(--sky);
    font-size: 25px;
  }
  .brand-mark .brand-sub { font-size: 17px; letter-spacing: 1px; }

  .divider {
    position: absolute;
    left: 312px; top: 78px;
    width: 1.5px; height: 210px;
    background: var(--sky);
  }

  .contact {
    position: absolute;
    left: 339px; top: 124px;
  }
  .contact__name {
    font-family: "DM Serif Display", serif;
    font-size: 29px;
    color: var(--navy);
    line-height: 1;
  }
  .contact__role {
    font-size: 15.5px;
    letter-spacing: 1px;
    color: var(--sky);
    margin-top: 4px;
  }
  .contact__list { list-style: none; margin-top: 10px; }
  .contact__list li {
    display: flex;
    align-items: center;
    gap: 9px;
    font-size: 15px;
    color: var(--ink);
    letter-spacing: 0.4px;
    height: 22px;
  }
  .contact__list svg { width: 13px; height: 13px; flex: none; }

  .experience-seal {
    position: absolute;
    left: 534px; top: 280px;
    width: 72px; height: 72px;
  }

  .back-url {
    position: absolute;
    left: 0; right: 0; top: 318px;
    text-align: center;
    font-size: 14px;
    letter-spacing: 5.5px;
    color: var(--sky);
  }
</style>
</head>
<body>

<section class="card card--front" aria-label="Business card front">
  <div class="brand-mark">Wrenfield<span class="brand-sub">Disability</span></div>
  <div class="divider"></div>

  <div class="contact">
    <h1 class="contact__name">MARTIN HALE</h1>
    <p class="contact__role">MANAGING DIRECTOR</p>
    <ul class="contact__list">
      <li>
        <svg viewBox="0 0 16 16" aria-hidden="true"><path d="M4 1.5 6.3 4.6 5 6.2c.9 2 2.6 3.7 4.6 4.6l1.6-1.3 3.1 2.3-1.1 2.4C7.6 14 2 8.4 1.7 2.6Z" fill="none" stroke="var(--gold)" stroke-width="1.5" stroke-linejoin="round"/></svg>
        224 555 0187
      </li>
      <li>
        <svg viewBox="0 0 16 16" aria-hidden="true"><g fill="none" stroke="var(--gold)" stroke-width="1.3"><circle cx="8" cy="8" r="6.5"/><ellipse cx="8" cy="8" rx="2.8" ry="6.5"/><path d="M1.5 8h13M2.5 4.8h11M2.5 11.2h11"/></g></svg>
        martin@wrenfielddisability.com
      </li>
      <li>
        <svg viewBox="0 0 16 16" aria-hidden="true"><rect x="1" y="3" width="14" height="10" fill="var(--gold)"/><path d="M1 3l7 5.5L15 3" fill="none" stroke="#fff" stroke-width="1.2"/></svg>
        www.wrenfielddisability.com
      </li>
    </ul>
  </div>

  <svg class="experience-seal" viewBox="0 0 72 72" aria-label="Over 35 years of experience">
    <defs><path id="seal-ring" d="M36 36m-27 0a27 27 0 1 1 54 0a27 27 0 1 1-54 0"/></defs>
    <text font-family="Mulish, sans-serif" font-size="7" font-weight="600" letter-spacing="1.6" fill="var(--navy)">
      <textPath href="#seal-ring">OVER 35 YEARS OF EXPERIENCE •</textPath>
    </text>
    <text x="36" y="37" text-anchor="middle" font-family="DM Serif Display, serif" font-size="15" fill="var(--navy)">35</text>
    <text x="36" y="48" text-anchor="middle" font-family="DM Serif Display, serif" font-size="9" fill="var(--navy)">YEARS</text>
  </svg>
</section>

<section class="card card--back" aria-label="Business card back">
  <div class="brand-mark">Wrenfield<span class="brand-sub">Disability</span></div>
  <p class="back-url">WWW.WRENFIELDDISABILITY.COM</p>
</section>

</body>
</html>
```